Executive Business Card for Healthcare Company [Need Today]

I need a business card design for a healthcare company. The only branding the company has thus far is a logo. The cards will be utilized by company executives. The design I envision will be vibrant and appealing but with a corporate feel. They shouldn't be too casual or playful. I would like to complete this project TODAY if possible.

Target Market(s)

Healthcare vendors, other executives in healthcare and pharmaceuticals

Industry/Entity Type

Pharmaceutical

Contact Information for Business Card

See attachment

Font styles to use
Serif
Sans Serif

Colors

Designer to choose colors to be used in the design.

```html
<!DOCTYPE html>
<html lang="en">
<head>
<meta charset="utf-8">
<title>Tavena Therapeutics – Business Card</title>
<link rel="stylesheet" href="https://fonts.googleapis.com/css2?family=Questrial&display=swap">
<style>
  :root {
    --page: #e4e2de;
    --card-top: #eef1f2;
    --card-bottom: #e3e6e6;
    --teal: #2b928f;
    --teal-dark: #1f7573;
    --logo-green: #4c9e78;
    --ink: #3a3a3a;
    --muted: #8a8a8a;
  }
  * { margin: 0; padding: 0; box-sizing: border-box; }
  html, body { width: 1200px; height: 970px; overflow: hidden; }
  body {
    background: var(--page);
    font-family: "Questrial", "Century Gothic", sans-serif;
    color: var(--ink);
    position: relative;
  }
  .card {
    position: absolute;
    left: 80px; top: 189px;
    width: 1040px; height: 592px;
    background: linear-gradient(160deg, var(--card-top), var(--card-bottom));
    box-shadow: 0 10px 30px rgba(0,0,0,0.15);
    overflow: hidden;
  }
  .side-band {
    position: absolute; left: 0; top: 0;
    width: 128px; height: 100%;
    background: linear-gradient(180deg, var(--teal-dark), var(--teal));
    border-right: 4px solid #f4f6f6;
  }
  .brand {
    position: absolute; left: 46px; top: 60px;
    display: flex; align-items: center;
  }
  .brand-mark {
    width: 146px; height: 146px; border-radius: 50%;
    background: #eef0ec;
    border: 4px solid var(--logo-green);
    box-shadow: 0 0 0 8px #eef0ec;
    flex: none;
  }
  .brand-divider {
    width: 2px; height: 72px; background: var(--muted);
    margin: 0 14px 0 14px;
  }
  .brand-name {
    font-size: 34px; line-height: 1.1; color: var(--teal);
  }
  .person { position: absolute; left: 222px; top: 355px; }
  .person-name { font-size: 30px; color: var(--teal); }
  .person-title { font-size: 25px; color: var(--ink); margin-top: 2px; }
  .rule {
    position: absolute; left: 224px; top: 432px;
    width: 757px; height: 2px; background: var(--teal);
  }
  .contacts {
    position: absolute; left: 222px; top: 452px;
    list-style: none; font-size: 25px; color: #555;
  }
  .contacts li { display: flex; align-items: center; height: 32px; }
  .contacts svg { width: 26px; height: 26px; margin-right: 8px; flex: none; }
  .address {
    position: absolute; left: 695px; top: 452px;
    font-size: 25px; line-height: 32px; font-style: normal;
  }
  .address .company { color: var(--teal); }
</style>
</head>
<body>
  <section class="card" aria-label="Business card">
    <div class="side-band"></div>

    <div class="brand">
      <div class="brand-mark" aria-hidden="true"></div>
      <div class="brand-divider"></div>
      <div class="brand-name">tavena therapeutics</div>
    </div>

    <div class="person">
      <div class="person-name">Daniel Hartley</div>
      <div class="person-title">Senior Director of Marketing</div>
    </div>

    <div class="rule"></div>

    <ul class="contacts">
      <li>
        <svg viewBox="0 0 26 26" aria-hidden="true"><circle cx="13" cy="13" r="11" fill="none" stroke="var(--teal)" stroke-width="2"/><rect x="9.5" y="6.5" width="7" height="13" rx="1.5" fill="none" stroke="var(--teal)" stroke-width="1.8"/></svg>
        555-210-4837
      </li>
      <li>
        <svg viewBox="0 0 26 26" aria-hidden="true"><circle cx="13" cy="13" r="11" fill="var(--teal)"/><path d="M7 11c0-2 2-3 6-3s6 1 6 3l-2 1-1-2h-6l-1 2z M8 13h10v4H8z" fill="#fff"/></svg>
        555-210-4900
      </li>
      <li>
        <svg viewBox="0 0 26 26" aria-hidden="true"><circle cx="13" cy="13" r="11" fill="none" stroke="var(--teal)" stroke-width="2"/><rect x="7" y="9" width="12" height="8" fill="none" stroke="var(--teal)" stroke-width="1.6"/><path d="M7 9l6 5 6-5" fill="none" stroke="var(--teal)" stroke-width="1.6"/></svg>
        dhartley@tavenarx.com
      </li>
    </ul>

    <address class="address">
      <div class="company">Tavena Therapeutics, LLC</div>
      <div>118 Laurel Park Avenue</div>
      <div>Millbrook, GA 30999</div>
    </address>
  </section>
</body>
</html>
```